IT company requires website redesign

I have an old boring website that I want to update - www.tvkb-example.net
I am a growing IT company beginning to look after more healthcare professionals such as medical and dental practices so a more professional look is required

Blue and orange are the company colours. See one of our local competitors for your reference and ideas - https://www.plinth-halvard.example.au

Target Market(s)

Medical, dental, professional, solicitors etc

Industry/Entity Type

It Support

Number of Pages Required

5+ page

Colors

Designer to choose colors to be used in the design.

Requirements
Must have
• Classy feel, simple with the 'less is more' approach
• On support page, links to support items, a couple more to come
• Reference to our technology partners
• Easy to read
Nice to have
• Company colours are blue with a little orange but I willing to consider new web colour schemes
• leave the rest to you

```html
<!DOCTYPE html>
<html lang="en">
<head>
<meta charset="utf-8">
<title>Cobalt Ridge Systems – IT Support</title>
<link href="https://fonts.googleapis.com/css2?family=Lato:wght@300;400;700&display=swap" rel="stylesheet">
<style>
  :root {
    --orange: #e8a42a;
    --hero-bg: #ececec;
    --ink: #222222;
    --nav-ink: #555555;
    --white: #ffffff;
    --brand-blue: #1f2a78;
  }
  * { box-sizing: border-box; margin: 0; padding: 0; }
  html, body { width: 1200px; height: 1200px; overflow: hidden; }
  body { font-family: "Lato", sans-serif; background: var(--white); color: var(--ink); position: relative; }

  .site-header {
    position: absolute; top: 0; left: 0; width: 1200px; height: 64px;
    background: var(--white); box-shadow: 0 3px 8px rgba(0,0,0,0.18); z-index: 2;
  }
  .brand {
    position: absolute; left: 56px; top: 20px;
    display: flex; align-items: center; gap: 8px;
    font-size: 17px; font-weight: 700; color: var(--brand-blue);
  }
  .brand-dot { width: 12px; height: 12px; border-radius: 50%; background: var(--orange); }
  .main-nav a {
    position: absolute; top: 21px; font-size: 16px; font-weight: 300;
    color: var(--nav-ink); text-decoration: none;
  }

  .hero { position: absolute; top: 64px; left: 0; width: 1200px; height: 432px; background: var(--hero-bg); }
  .hero-title { position: absolute; left: 143px; top: 156px; font-size: 29px; font-weight: 700; line-height: 35px; color: var(--ink); letter-spacing: 0.3px; }
  .hero-sub { position: absolute; left: 143px; top: 251px; font-size: 21px; font-weight: 400; line-height: 25px; color: var(--ink); letter-spacing: 0.3px; }
  .hero-art {
    position: absolute; left: 584px; top: 104px; width: 376px; height: 264px; border-radius: 24px;
    background: radial-gradient(ellipse at 55% 50%, #fafafa 0%, #f3f3f3 45%, var(--hero-bg) 75%);
  }

  .savings { position: absolute; top: 496px; left: 0; width: 1200px; height: 427px; background: var(--orange); color: var(--white); text-align: center; }
  .savings-title { position: absolute; top: 36px; width: 100%; font-size: 37px; font-weight: 700; letter-spacing: 0.5px; }
  .savings-text { position: absolute; top: 107px; width: 100%; font-size: 18px; line-height: 23px; font-weight: 400; }
  .service { position: absolute; width: 220px; margin-left: -110px; text-align: center; }
  .service svg { display: block; margin: 0 auto; }
  .service-label { display: block; font-size: 16px; font-weight: 400; color: var(--white); opacity: 0.95; }
  .carousel-dots { position: absolute; top: 381px; left: 570px; display: flex; gap: 13px; }
  .carousel-dots span { width: 11px; height: 11px; border-radius: 50%; background: rgba(255,255,255,0.45); }
  .carousel-dots span.active { background: var(--white); }

  .help { position: absolute; top: 923px; left: 0; width: 1200px; height: 277px; text-align: center; }
  .help-line { position: absolute; top: 72px; width: 100%; font-size: 30px; font-weight: 400; color: var(--ink); }
  .help-line .accent { color: var(--orange); }
  .cta {
    position: absolute; left: 481px; top: 154px; width: 238px; height: 57px; border-radius: 7px;
    background: var(--orange); color: var(--white); font-size: 29px; font-weight: 400;
    display: flex; align-items: center; justify-content: center; text-decoration: none;
  }
</style>
</head>
<body>
  <header class="site-header">
    <div class="brand"><span class="brand-dot"></span>Cobalt Ridge Systems</div>
    <nav class="main-nav">
      <a href="#" style="left:766px">Services</a>
      <a href="#" style="left:860px">Support</a>
      <a href="#" style="left:954px">About Us</a>
      <a href="#" style="left:1048px">Contact Us</a>
    </nav>
  </header>

  <section class="hero">
    <h1 class="hero-title">Welcome to<br>Cobalt Ridge Systems!</h1>
    <p class="hero-sub">A better tomorrow, starts through<br>intelligent use of technology today!</p>
    <div class="hero-art" role="img" aria-label="Illustration of white clouds with an orange sun in a pale grey sky"></div>
  </section>

  <section class="savings">
    <h2 class="savings-title">How we can save you $$$</h2>
    <p class="savings-text">Cobalt Ridge Systems is your one stop shop for all your technological needs.<br>Often providing savings of hundreds, even thousands of dollars.</p>

    <div class="service" style="left:264px; top:214px">
      <svg width="140" height="64" viewBox="0 0 140 64"><path fill="#fff" d="M20 64a20 20 0 0 1-4-39.6A28 28 0 0 1 70 12a18 18 0 0 1 30 10h12a17 17 0 0 1 0 42Z"/></svg>
      <span class="service-label" style="margin-top:18px">Cloud Solutions</span>
    </div>
    <div class="service" style="left:524px; top:218px">
      <svg width="66" height="66" viewBox="0 0 66 66"><path fill="#fff" d="M25 0h16v25h25v16H41v25H25V41H0V25h25Z"/></svg>
      <span class="service-label" style="margin-top:14px">Medical Software &amp; Tools</span>
    </div>
    <div class="service" style="left:768px; top:214px">
      <svg width="84" height="68" viewBox="0 0 84 68"><rect x="40" y="0" width="20" height="4" fill="#fff"/><rect x="47" y="4" width="6" height="18" fill="#fff"/><rect x="22" y="22" width="60" height="24" rx="5" fill="#fff" transform="rotate(-20 52 34)"/><path fill="#fff" d="M2 44l16-6 6 14-16 16Z"/></svg>
      <span class="service-label" style="margin-top:16px">CCTV Solutions</span>
    </div>
    <div class="service" style="left:972px; top:208px">
      <svg width="64" height="68" viewBox="0 0 64 68"><g fill="#fff"><rect y="0" width="64" height="19" rx="3"/><rect y="24" width="64" height="19" rx="3"/><rect y="48" width="64" height="19" rx="3"/></g><g fill="var(--orange)"><circle cx="6" cy="9.5" r="1.6"/><circle cx="12" cy="9.5" r="1.6"/><circle cx="18" cy="9.5" r="1.6"/><circle cx="58" cy="9.5" r="1.6"/><circle cx="6" cy="33.5" r="1.6"/><circle cx="12" cy="33.5" r="1.6"/><circle cx="18" cy="33.5" r="1.6"/><circle cx="58" cy="33.5" r="1.6"/><circle cx="6" cy="57.5" r="1.6"/><circle cx="12" cy="57.5" r="1.6"/><circle cx="18" cy="57.5" r="1.6"/><circle cx="58" cy="57.5" r="1.6"/></g></svg>
      <span class="service-label" style="margin-top:32px">PABX System</span>
    </div>

    <div class="carousel-dots"><span class="active"></span><span></span><span></span></div>
  </section>

  <section class="help">
    <p class="help-line"><span class="accent">Cobalt Ridge Systems</span> – We are here to help you!</p>
    <a class="cta" href="#">Contact Us</a>
  </section>
</body>
</html>
```